ALL TEXT Social Media Graphics

We are looking for a series of social media graphics for Instagram (new size: 4:5 (1080 x 1350 pixels) ratio that are ALL TEXT. We want the following quotes below on each graphic; one quote per graphic. AND, In very small letters at the bottom of each graphic, add @PaulaWrenLive
The look and feel of these graphics should be complimentary to the color palette attached below; but keep them simple. But the design is up to you; at the end of this document, I provided various samples of all text graphics that I like as examples.
The Quotes are in the attached WORD document
women trying to lose weight

```html
<!DOCTYPE html>
<html lang="en">
<head>
<meta charset="utf-8">
<title>Sun Girl Summer Shapeup – Social Quote Set</title>
<link href="https://fonts.googleapis.com/css2?family=Archivo+Black&family=Baloo+2:wght@600;700;800&family=Bitter:wght@700&family=Exo+2:wght@300&family=Montserrat:ital,wght@0,300;0,400;0,600;0,700;0,800;1,400&family=Oswald:wght@600;700&family=Teko:wght@300;400;500&display=swap" rel="stylesheet">
<style>
  :root {
    --board: #9a9b9d;
    --magenta: #d4006a;
    --magenta-deep: #c8005f;
    --pink-glow: #ef5b92;
    --pink-bright: #f0449a;
    --blush: #fde2ee;
    --white: #ffffff;
  }
  * { margin: 0; padding: 0; box-sizing: border-box; }
  html, body { width: 1197px; height: 1200px; overflow: hidden; }
  body { background: var(--board); position: relative; font-family: "Montserrat", sans-serif; }

  .post { position: absolute; width: 268px; height: 334px; overflow: hidden; }
  .post--pink {
    color: var(--white);
    background:
      radial-gradient(circle at 85% 12%, var(--pink-glow) 0%, rgba(239,91,146,0) 55%),
      linear-gradient(180deg, #de1f79 0%, var(--magenta) 100%);
  }
  .post--white {
    color: var(--magenta);
    background: linear-gradient(180deg, var(--white) 0%, var(--white) 72%, var(--blush) 100%);
  }
  .block { position: absolute; left: 22px; white-space: nowrap; }
  .handle { position: absolute; left: 28px; top: 307px; font: 600 11px/1 "Montserrat", sans-serif; }
  .post--white .handle { color: var(--magenta-deep); }

  .col-1 { left: 28px; } .col-2 { left: 319px; } .col-3 { left: 610px; } .col-4 { left: 901px; }
  .row-1 { top: 78px; } .row-2 { top: 433px; } .row-3 { top: 788px; }

  .serif-head { font: 700 20px/22px "Bitter", serif; color: var(--magenta-deep); }
  .condensed { font-family: "Teko", sans-serif; font-weight: 400; }
  .heavy-condensed { font-family: "Oswald", sans-serif; font-weight: 700; letter-spacing: -0.3px; transform: scaleX(0.82); transform-origin: left; }
  .rounded { font-family: "Baloo 2", sans-serif; }
  .cta-sm { font-size: 14px; line-height: 20px; font-weight: 400; }
  .accent { color: var(--pink-bright); }
  .accent-bold { color: var(--pink-bright); font-weight: 700; }
  .big-word { font: 800 27px/1 "Montserrat", sans-serif; letter-spacing: 0.5px; }
  .small-label { font: 400 15px/1 "Montserrat", sans-serif; padding-left: 36px; display: block; }
</style>
</head>
<body>

<!-- Row 1 -->
<article class="post post--white col-1 row-1">
  <h2 class="block serif-head" style="top:24px">You can absolutely be<br>down 20–30 pounds<br>by end of summer.</h2>
  <p class="block" style="top:118px;left:25px;font:600 17px/25px 'Montserrat',sans-serif">All it takes is the<br>right plan—and<br>you’ve found it.</p>
  <p class="block cta-sm accent" style="top:209px;left:26px">Comment “Sun Girl”<br>for the Sun Girl<br>Summer Shapeup!</p>
  <span class="handle">@PaulaWrenLive</span>
</article>

<article class="post post--pink col-2 row-1">
  <h2 class="block condensed" style="left:20px;top:22px;font-size:35px;line-height:35px;font-weight:300">you don’t need<br>another diet—you need<br>a system that works.</h2>
  <p class="block" style="left:19px;top:150px;font:700 18px/25px 'Montserrat',sans-serif">Drop 30 pounds<br>with the Sun Girl<br>Summer Shapeup.</p>
  <p class="block cta-sm" style="left:19px;top:240px">Comment <b>“Summer”</b><br>to start now.</p>
  <span class="handle" style="left:19px">@PaulaWrenLive</span>
</article>

<article class="post post--white col-3 row-1">
  <h2 class="block rounded" style="left:21px;top:20px;font-weight:700;font-size:21px;line-height:27px">This summer ain’t<br>over—and neither are<br>your body goals.</h2>
  <p class="block accent" style="left:21px;top:130px;font:300 21px/26px 'Exo 2',sans-serif">Drop 30 pounds<br>with the Sun Girl<br>Summer Shapeup.</p>
  <p class="block" style="left:21px;top:227px;font:400 15px/22px 'Montserrat',sans-serif">Comment <b><i>“Sun Girl”</i></b><br>to get the plan</p>
  <span class="handle" style="left:21px">@PaulaWrenLive</span>
</article>

<article class="post post--pink col-4 row-1">
  <h2 class="block condensed" style="top:20px;font-size:29px;line-height:32px;font-weight:300"><span style="font-weight:500">If your goal is a tiny<br>waist, flat belly,</span><br>and 30 pounds<br>down—this is the plan.</h2>
  <p class="block" style="left:23px;top:206px;font:400 15px/22px 'Montserrat',sans-serif">Comment <b><i>“Summer”</i></b><br>to join the <b>Sun Girl</b><br><b>Summer</b> Shapeup!</p>
  <span class="handle" style="left:20px">@PaulaWrenLive</span>
</article>

<!-- Row 2 -->
<article class="post post--pink col-1 row-2">
  <h2 class="block condensed" style="left:20px;top:22px;font-size:28px;line-height:29px;font-weight:400">There’s still time<br>to drop the 30 pounds<br>and slay this summer.</h2>
  <p class="block" style="top:132px;font:400 16px/26px 'Archivo Black',sans-serif;letter-spacing:0.3px">THE SUN GIRL<br>SUMMER SHAPEUP<br>HAS THE BLUEPRINT.</p>
  <p class="block" style="left:25px;top:232px;font:300 italic 22px/1 'Montserrat',sans-serif">Comment</p>
  <p class="block" style="top:258px;font:700 16px/1 'Montserrat',sans-serif">“Sun Girl”!</p>
  <span class="handle">@PaulaWrenLive</span>
</article>

<article class="post post--white col-2 row-2">
  <h2 class="block heavy-condensed" style="left:20px;top:30px;font-size:24px;line-height:34px">Snatched waist, flat tummy,<br>30 pounds lighter —that’s<br>what the Sun Girl Summer<br>Shapeup Challenge delivers.</h2>
  <p class="block" style="left:22px;top:205px;font:300 21px/27px 'Montserrat',sans-serif">Comment <span class="accent-bold">“Sun Girl”</span><br>to get the plan</p>
  <span class="handle" style="left:19px">@PaulaWrenLive</span>
</article>

<article class="post post--pink col-3 row-2">
  <h2 class="block condensed" style="left:18px;top:26px;font-size:32px;line-height:33px;font-weight:400">Nothing feels better<br>than seeing that scale<br>drop week after week.</h2>
  <p class="block" style="top:143px;font:700 18px/25px 'Montserrat',sans-serif">Let’s lose up to<br>30 pounds this<br>summer—together.</p>
  <p class="block" style="left:23px;top:232px;font:400 13px/18px 'Montserrat',sans-serif">Comment <b>“Summer”</b> to<br>join the Sun Girl Summer<br>Shapeup!</p>
  <span class="handle" style="left:21px">@PaulaWrenLive</span>
</article>

<article class="post post--white col-4 row-2">
  <h2 class="block" style="left:21px;top:34px;font:400 italic 19px/27px 'Montserrat',sans-serif">Sis, we’re dropping<br>belly flat and saying<br>goodbye to stubborn<br>pounds.</h2>
  <p class="block heavy-condensed" style="left:21px;top:166px;font-weight:600;font-size:22px;line-height:30px">Join the Sun Girl<br>Summer Shapeup –<br>Comment “Summer”!</p>
  <span class="handle" style="left:20px">@PaulaWrenLive</span>
</article>

<!-- Row 3 -->
<article class="post post--pink col-2 row-3">
  <h2 class="block rounded" style="left:20px;top:26px;font-weight:800;font-size:20px;line-height:26px">Don’t wait ‘til next<br>summer to get right.<br>The time is now.</h2>
  <p class="block condensed" style="left:18px;top:124px;font-size:30px;line-height:29px;font-weight:400">Drop 30 pounds<br>with the Sun Girl<br>Summer Shapeup.</p>
  <p class="block" style="left:19px;top:250px"><span class="small-label">Comment</span><span class="big-word">“Summer”!</span></p>
  <span class="handle" style="left:19px">@PaulaWrenLive</span>
</article>

<article class="post post--white col-3 row-3">
  <h2 class="block" style="left:21px;top:30px;font:400 19px/27px 'Montserrat',sans-serif">You’ve got <b>8 weeks</b><br>and the <b>perfect plan</b><br><b>to drop 30 pounds.</b></h2>
  <p class="block rounded accent" style="left:21px;top:130px;font-weight:700;font-size:18px;line-height:25px">Let’s get snatched this<br>summer with the<br>Sun Girl Summer<br>Shapeup.</p>
  <p class="block" style="left:21px;top:250px;color:var(--magenta-deep)"><span class="small-label">Comment</span><span class="big-word">“Summer”!</span></p>
  <span class="handle" style="left:21px">@PaulaWrenLive</span>
</article>

</body>
</html>
```